New Zealand Luggage Importer Needs Business Cards

We need professional, creative and fashionable business cards created.
We are based in New Zealand and import and distribute high-end, quality, fashionable and durable luggage.
We pride ourselves on selling the very best quality luggage, second only to 1 brand (which we won't mention here)...we use the same manufacturer. However, our prices are much more reasonable.
Industry/Entity Type
Business
Contact Information for Business Card
Mark Dunsley
027 512 4068
3/17 Harlow Street, Pinecrest Flats, Auckland, 0614
PO Box 204377, Fernside, Auckland 0731
09-528-3916
sales@brivancases.co.nz / www.brivancases.co.nz

```html
<!DOCTYPE html>
<html lang="en">
<head>
<meta charset="utf-8">
<title>Brivan Cases – Business Card</title>
<link href="https://fonts.googleapis.com/css2?family=Jost:wght@400;500;600&display=swap" rel="stylesheet">
<style>
  :root {
    --stage: #1d1d1f;
    --card: #f4f4f2;
    --ink: #1a1a1a;
    --ink-soft: #3a3a3a;
    --gold: #c9a233;
    --gold-light: #ecd47a;
    --gold-deep: #a9831f;
    --band-dark: #1f1f20;
  }
  * { box-sizing: border-box; margin: 0; padding: 0; }
  html, body { width: 1200px; height: 800px; overflow: hidden; }
  body {
    background: var(--stage);
    font-family: "Jost", sans-serif;
    position: relative;
  }
  .card {
    position: absolute;
    top: 245px;
    width: 540px;
    height: 310px;
    background: var(--card);
    overflow: hidden;
    box-shadow: 0 10px 30px rgba(0,0,0,.5);
  }
  .card--back { left: 40px; }
  .card--front { left: 620px; }
  .card__bands { position: absolute; inset: 0; width: 100%; height: 100%; }

  .wordmark {
    position: absolute;
    font-weight: 600;
    letter-spacing: 0.06em;
    color: var(--ink);
    white-space: nowrap;
  }
  .card--back .wordmark { left: 40px; top: 142px; font-size: 20px; }
  .card--front .wordmark { left: 50%; top: 50%; transform: translate(-50%, -50%); font-size: 34px; }

  .contact { position: absolute; left: 262px; top: 42px; width: 260px; }
  .contact__name { font-size: 26px; font-weight: 400; color: var(--ink); line-height: 1; }
  .contact__address { margin-top: 10px; font-size: 9.5px; line-height: 1.45; color: var(--ink-soft); }
  .contact__list { list-style: none; margin-top: 30px; margin-left: 38px; }
  .contact__item { display: flex; align-items: center; gap: 12px; height: 26px; font-size: 13px; color: var(--ink); }
  .contact__icon { width: 17px; height: 17px; flex: none; }
</style>
</head>
<body>

<section class="card card--back" aria-label="Business card, contact side">
  <svg class="card__bands" viewBox="0 0 540 310" preserveAspectRatio="none" aria-hidden="true">
    <defs>
      <linearGradient id="goldBack" x1="0" y1="0" x2="1" y2="0">
        <stop offset="0" stop-color="var(--gold-deep)"/>
        <stop offset=".5" stop-color="var(--gold-light)"/>
        <stop offset="1" stop-color="var(--gold)"/>
      </linearGradient>
      <linearGradient id="panelTint" x1="0" y1="0" x2="1" y2="0">
        <stop offset="0" stop-color="#f6f6f4"/>
        <stop offset="1" stop-color="#ece6d6"/>
      </linearGradient>
    </defs>
    <rect x="0" y="0" width="240" height="310" fill="url(#panelTint)"/>
    <polygon points="200,0 250,0 250,18 200,10" fill="var(--band-dark)"/>
    <polygon points="250,0 540,0 540,4 430,18 250,18" fill="url(#goldBack)"/>
    <polygon points="250,18 262,18 262,292 250,292" fill="url(#goldBack)" opacity=".55"/>
    <polygon points="150,310 250,292 250,310" fill="var(--band-dark)"/>
    <polygon points="250,292 480,292 540,306 540,310 250,310" fill="url(#goldBack)"/>
  </svg>

  <div class="wordmark">BRIVAN CASES</div>

  <div class="contact">
    <p class="contact__name">Mark Dunsley</p>
    <p class="contact__address">3/17 Harlow Street, Pinecrest Flats, Auckland, 0614<br>PO Box 204377, Fernside, Auckland 0731</p>
    <ul class="contact__list">
      <li class="contact__item">
        <svg class="contact__icon" viewBox="0 0 20 20" aria-hidden="true"><circle cx="10" cy="10" r="9" fill="none" stroke="var(--gold)" stroke-width="1.2"/><path d="M7 5.5l2 2-1 1.2a6 6 0 0 0 3.3 3.3l1.2-1 2 2-1.3 1.5C9.5 14 6 10.5 5.5 6.8z" fill="var(--gold)"/></svg>
        <span>027 512 4068</span>
      </li>
      <li class="contact__item">
        <svg class="contact__icon" viewBox="0 0 20 20" aria-hidden="true"><circle cx="10" cy="10" r="9" fill="none" stroke="var(--gold)" stroke-width="1.2"/><rect x="5.5" y="7" width="9" height="6.5" fill="none" stroke="var(--gold)" stroke-width="1.1"/><path d="M5.5 7l4.5 3.5L14.5 7" fill="none" stroke="var(--gold)" stroke-width="1.1"/></svg>
        <span>sales@brivancases.co.nz</span>
      </li>
      <li class="contact__item">
        <svg class="contact__icon" viewBox="0 0 20 20" aria-hidden="true"><circle cx="10" cy="10" r="8" fill="none" stroke="var(--gold)" stroke-width="1.2"/><ellipse cx="10" cy="10" rx="3.5" ry="8" fill="none" stroke="var(--gold)" stroke-width="1"/><path d="M2 10h16M3.5 6h13M3.5 14h13" stroke="var(--gold)" stroke-width="1"/></svg>
        <span>www.brivancases.co.nz</span>
      </li>
    </ul>
  </div>
</section>

<section class="card card--front" aria-label="Business card, brand side">
  <svg class="card__bands" viewBox="0 0 540 310" preserveAspectRatio="none" aria-hidden="true">
    <defs>
      <linearGradient id="goldFront" x1="0" y1="0" x2="1" y2="0">
        <stop offset="0" stop-color="var(--gold-deep)"/>
        <stop offset=".45" stop-color="var(--gold-light)"/>
        <stop offset="1" stop-color="var(--gold)"/>
      </linearGradient>
    </defs>
    <polygon points="150,0 300,0 300,28 150,6" fill="var(--band-dark)"/>
    <polygon points="300,0 540,0 540,10 430,28 300,28" fill="url(#goldFront)"/>
    <polygon points="0,290 130,270 250,270 250,310 0,310" fill="var(--band-dark)"/>
    <polygon points="250,270 400,270 540,302 540,310 250,310" fill="url(#goldFront)"/>
  </svg>

  <div class="wordmark">BRIVAN CASES</div>
</section>

</body>
</html>
```